Wordpress Design for Interactive Marketing Agency

We are looking to have a WP theme designed for our company, Bright Harbor Media. We are an online marketing firm specializing in SEO, Paid Search/PPC, Analytics and a number of other marketing channels.
We have a logo and tag line. We also have a rough and unloved design to work from as a way to illustrate the content needs of the homepage. We would like an interactive slider on the homepage which displays text and image content describing our services and our value props/solution positioning. Layering content is also something we'd like to incorporate in a block or two on the page, whether it be tabs, window shades, rotating or mouse-over type div swapping, scrolling news box, etc.
The design also needs to be able to transition to a less portal-like feel (re: the homepage) to a page design that houses a description for each of our services, an about page, privacy page, etc.
So, in the spirit of the typical WP construct, there would be a consistent header and footer, with a main content div that is flexible and eye-catching.
Three column design for the homepage feels right, but that's not a requirement. For the rest of the pages one or two columns seems like the right layout. Again, is this open to design.
To see what we've put together as a concept visit this page:
www.brightharbormedia.example/design/
Notes: most folks didn't care for the opaque gun in the background. Though, a subtle, muted background image would be a welcome design element. Keep in mind that these images are only for illustrating the content needs. We are not expecting anything that looks like these concepts. In fact, they didn't appeal to most of us.
Also included is a third design that we kind of liked (probably could live without the page curls, though). Modern sophistication that isn't stuffy but doesn't get too juvenile is what we're wanting. If there's a way to complement the power colors of our logo and attain a style that's lively, digerati in spirit and alluring, then that's what we would like to arrive at.
To get the latest logo:
http://brightharbormedia.example/design/Logo-Rework.png
The logo can be rearranged as needed.
I have also attached the rough designs we put together and the logo.
We really don't have any strong restrictions or absolutes as far as how the design turns out. We just want something that looks great and captures the spirit of the business/brand. The visuals could definitely benefit from a human element, or a splashy graphic or something festive, technically inclined and/or inclusive.
Updates
Project Deadline Extended
Reason: I am trying to make the project a little more accessible for designers by extending it a bit. I realize that the process can sometimes take several days, and if this allows for more submissions, there are no complaints here.
Hi Designers,
Target Market(s)
Medium-sized, regional businesses
Industry/Entity Type
Marketing
Requirements
Must have
- Theme must accomodate widgets, permalinks and all of the common WP page enhancements and taxonomy options.
Nice to have
- Most of the text on the page should be true text if possible (for SEO purposes, etc.). The ability to layer text content is also desirable, so having content blocks that use z-indexed divs would be ideal. Theme should accommodate widgets, permalinks and all of the common WP page enhancements and taxonomy options.

```html
<!DOCTYPE html>
<html lang="en">
<head>
<meta charset="utf-8">
<title>Bright Harbor Media — Online Marketing</title>
<link href="https://fonts.googleapis.com/css2?family=Ubuntu:wght@400;500;700&family=Oswald:wght@500;700&family=Arimo:wght@400;700&family=Noto+Serif:wght@400;700&display=swap" rel="stylesheet">
<style>
:root{
  --orange:#e8501f;
  --orange-light:#f47a2a;
  --red:#d32f1e;
  --ink:#2b2b2b;
  --grey-text:#555;
  --muted:#888;
  --page:#e4e4e4;
  --card:#efefef;
  --nav-top:#5b5b5b;
  --nav-bottom:#3a3a3a;
  --footer:#2a3140;
  --footer-dark:#232935;
  --footer-text:#c9ced8;
  --field:#f1f1f1;
}
*{box-sizing:border-box;margin:0;padding:0}
html,body{width:960px;height:1200px;overflow:hidden}
body{position:relative;background:var(--page);font-family:"Arimo",Arial,sans-serif;color:var(--ink)}
.abs{position:absolute}

/* Header */
.site-header{position:absolute;left:0;top:0;width:960px;height:111px;background:linear-gradient(#ffffff,#ececec)}
.brand{left:92px;top:48px;display:flex;align-items:center;gap:8px}
.brand-dot{width:22px;height:22px;border-radius:50%;background:var(--orange)}
.brand-name{font-family:"Ubuntu",sans-serif;font-weight:700;font-size:19px;color:var(--orange);letter-spacing:.5px}
.brand-tag{left:162px;top:80px;font-family:"Ubuntu",sans-serif;font-size:10px;color:var(--grey-text);font-weight:500}
.hotline{left:592px;top:4px;font-family:"Oswald",sans-serif;font-weight:700;font-size:20px;color:#666;white-space:nowrap}
.hotline b{color:var(--orange)}
.badge{top:51px;width:52px;height:51px;border-radius:3px;border:1px solid #c7d3e0;background:linear-gradient(#f5f8fc,#dce6f0)}

/* Navigation */
.main-nav{left:0;top:111px;width:960px;height:29px;background:linear-gradient(var(--nav-top),var(--nav-bottom))}
.main-nav a{position:absolute;top:0;height:29px;line-height:29px;color:#fff;font-family:"Ubuntu",sans-serif;font-weight:500;font-size:11px;text-decoration:none}
.nav-divider{position:absolute;top:0;width:1px;height:29px;background:#2e2e2e;box-shadow:1px 0 #6a6a6a}
.main-nav .nav-home{left:82px;width:92px;text-align:center;background:var(--orange);top:-7px;height:36px;line-height:44px}

/* Hero */
.hero{left:0;top:140px;width:960px;height:275px;background:radial-gradient(ellipse at 55% 10%,var(--orange-light),var(--orange) 55%,#c93a1b)}
.panel{background:#fff;border-radius:8px;box-shadow:0 2px 4px rgba(0,0,0,.25)}
.panel-title{font-family:"Ubuntu",sans-serif;font-weight:500;font-size:18px;color:var(--ink)}
.panel-title em{font-style:normal;color:var(--orange)}
.icon-disc{width:30px;height:30px;border-radius:50%;background:radial-gradient(circle at 40% 35%,var(--orange-light),var(--red));border:3px solid #fff;box-shadow:0 1px 3px rgba(0,0,0,.35)}
.rule{height:1px;background:repeating-linear-gradient(90deg,#bbb 0 2px,transparent 2px 4px)}
.field-label{font-size:11px;color:#444;text-align:right;width:60px}
.field{background:var(--field);border:1px solid #cfcfcf;border-radius:11px;box-shadow:inset 0 1px 2px rgba(0,0,0,.12)}
.pill-btn{border-radius:14px;background:linear-gradient(#f26a3a,#c9281a);border:2px solid #fff;box-shadow:0 0 0 1px var(--red);color:#fff;font-family:"Ubuntu",sans-serif;font-weight:700;font-size:14px;text-align:center}
.hero-head{left:349px;top:172px;font-family:"Ubuntu",sans-serif;font-weight:500;font-size:20px;line-height:29px;color:#fff;letter-spacing:.5px}
.hero-head b{color:#111;font-weight:700}
.hero-quote{left:349px;top:263px;font-family:"Ubuntu",sans-serif;font-weight:500;font-size:13px;line-height:29px;color:#fff;letter-spacing:.5px}
.quote-btn{left:357px;top:350px;width:235px;height:36px;border-radius:18px;background:linear-gradient(#fff,#dcdcdc);box-shadow:0 2px 4px rgba(0,0,0,.3);font-family:"Ubuntu",sans-serif;font-size:15px;color:#333;line-height:36px;padding-left:12px}
.quote-btn b{color:var(--orange)}
.mail-tile{left:531px;top:330px;width:46px;height:46px;border-radius:6px;background:linear-gradient(#fff,#ddd);box-shadow:0 2px 4px rgba(0,0,0,.35)}
.hero-art{left:632px;top:170px;width:242px;height:218px;background:linear-gradient(135deg,#f4f6fa,#cdd7e4 60%,#9aa6b4);border-radius:2px;box-shadow:0 3px 6px rgba(0,0,0,.3)}

/* Sidebar */
.section-title{font-family:"Ubuntu",sans-serif;font-weight:500;font-size:18px;color:var(--ink)}
.section-title em{font-style:normal;color:var(--orange)}
.cat-list{left:87px;top:471px;width:197px;list-style:none}
.cat-list li{height:28.8px;line-height:28.8px;font-size:10.5px;letter-spacing:.2px;white-space:nowrap}
.cat-main{background:linear-gradient(#f0622b,#d63a1c);color:#fff;border-bottom:1px solid #fff;padding-left:22px;position:relative}
.cat-main::before{content:"";position:absolute;left:6px;top:9px;width:10px;height:10px;background:#fff;border-radius:1px}
.cat-main::after{content:"+";position:absolute;left:7px;top:0;width:8px;text-align:center;color:var(--orange);font-weight:700;font-size:11px}
.cat-sub{background:#fff;color:#333;padding-left:22px;border-bottom:1px solid #eee}

/* Content */
.intro{left:318px;top:483px;width:564px;font-size:9.6px;line-height:16px;color:#555;letter-spacing:.3px}
.intro p{margin-bottom:7px}
.intro strong{color:#333;font-weight:700}
.points{left:323px;top:580px;list-style:none;font-family:"Noto Serif",serif;font-size:10.5px}
.points li{height:22.4px;display:flex;align-items:center;gap:9px;color:#888}
.points b{color:#222}
.num{width:15px;height:15px;border-radius:50%;background:var(--red);color:#fff;font-size:8px;text-align:center;line-height:15px;flex:none}
.view-more{left:741px;top:724px;font-size:10px;font-weight:700;color:var(--red)}
.card{top:758px;width:181px;height:175px;background:var(--card);border:1px solid #fff;border-radius:7px;box-shadow:0 1px 3px rgba(0,0,0,.18)}
.card-title{position:absolute;left:38px;top:12px;font-family:"Ubuntu",sans-serif;font-weight:500;font-size:14px;color:#333;white-space:nowrap}
.card-title em{font-style:normal;color:var(--orange)}
.card .icon-disc{position:absolute;left:6px;top:8px;width:24px;height:24px;border-width:2px}
.card .rule{position:absolute;left:10px;right:10px;top:34px}
.card-img{position:absolute;left:12px;top:45px;width:157px;height:75px}
.card-text{position:absolute;left:11px;right:14px;top:128px;font-size:9.6px;line-height:16px;color:#444;letter-spacing:.3px}
.card-text b{color:var(--red);float:right}

/* Footer */
.site-footer{left:0;top:1005px;width:960px;height:195px;background:var(--footer)}
.footer-band{left:0;top:1005px;width:960px;height:49px;background:var(--footer-dark)}
.footer-title{top:1025px;font-family:"Ubuntu",sans-serif;font-size:14.5px;font-weight:500;color:#aeb6c4}
.footer-text{font-size:10.4px;line-height:17px;color:var(--footer-text)}
.footer-text .hl{color:#8fa6c8}
.tweet-date{font-size:9.6px;color:#aeb6c4}
.msg-icon{width:22px;height:20px}
.signup{left:627px;top:1109px;width:247px;height:29px;background:#fff;border-radius:3px;box-shadow:0 0 0 2px #dfe3ea}
.signup span{position:absolute;left:10px;top:7px;font-size:11px;font-style:italic;color:#999}
.signup b{position:absolute;right:3px;top:3px;width:63px;height:23px;border-radius:3px;background:linear-gradient(#8fd0ef,#4da8d6);color:#123;font-size:11px;line-height:23px;text-align:center}
.footer-sep{height:1px;background:repeating-linear-gradient(90deg,#4a5366 0 2px,transparent 2px 4px)}
.footer-links{right:86px;top:1176px;font-size:10.4px;color:var(--footer-text);word-spacing:6px}
</style>
</head>
<body>

<header class="site-header">
  <div class="abs brand"><span class="brand-dot"></span><span class="brand-name">BRIGHT HARBOR MEDIA</span></div>
  <div class="abs brand-tag">Online Marketing. In Focus.</div>
  <div class="abs hotline">1800-555-0142 <b>Get a Free Audit !</b></div>
  <div class="abs badge" style="left:750px" role="img" aria-label="Partner certification badge"></div>
  <div class="abs badge" style="left:811px" role="img" aria-label="Advertising credit offer badge"></div>
</header>

<nav class="abs main-nav">
  <a class="nav-home" href="#">Home page</a>
  <span class="nav-divider" style="left:175px"></span>
  <a href="#" style="left:216px">Paid Search</a>
  <span class="nav-divider" style="left:303px"></span>
  <a href="#" style="left:332px">Display Ads</a>
  <span class="nav-divider" style="left:418px"></span>
  <a href="#" style="left:447px">Analytics</a>
  <span class="nav-divider" style="left:520px"></span>
  <a href="#" style="left:547px">Performance</a>
  <span class="nav-divider" style="left:639px"></span>
  <a href="#" style="left:664px">Contact&nbsp; Us</a>
</nav>

<section class="abs hero"></section>

<!-- Contact form -->
<div class="abs panel" style="left:94px;top:154px;width:225px;height:232px"></div>
<div class="abs icon-disc" style="left:100px;top:158px"></div>
<svg class="abs" style="left:108px;top:168px" width="16" height="12" viewBox="0 0 16 12"><rect x="0.5" y="0.5" width="15" height="11" fill="#fff"/><path d="M1 1l7 6 7-6" stroke="#d32f1e" fill="none" stroke-width="1.5"/></svg>
<div class="abs panel-title" style="left:140px;top:163px"><em>Contact</em> Us</div>
<div class="abs rule" style="left:140px;top:191px;width:160px"></div>
<div class="abs field-label" style="left:98px;top:212px">Name :</div>
<div class="abs field" style="left:174px;top:207px;width:131px;height:21px"></div>
<div class="abs field-label" style="left:98px;top:241px">Email :</div>
<div class="abs field" style="left:173px;top:236px;width:131px;height:21px"></div>
<div class="abs field-label" style="left:98px;top:269px">Phone :</div>
<div class="abs field" style="left:173px;top:264px;width:131px;height:21px"></div>
<div class="abs field-label" style="left:98px;top:298px">Question :</div>
<div class="abs field" style="left:172px;top:293px;width:133px;height:57px;border-radius:12px"></div>
<div class="abs pill-btn" style="left:206px;top:372px;width:87px;height:25px;line-height:22px">Send</div>

<h1 class="abs hero-head">The Complete <b>ONLINE</b><br>Marketing Solution for<br>Small <b>BUSINESS WEBSITES</b></h1>
<p class="abs hero-quote">″Get a big online presence and more<br>sales leads in 30 minutes″</p>
<div class="abs quote-btn">Request a <b>Quote</b></div>
<div class="abs mail-tile">
  <svg width="46" height="46" viewBox="0 0 46 46"><rect x="10" y="13" width="26" height="19" fill="#fff" stroke="#d32f1e" stroke-width="2"/><path d="M10 13l13 11 13-11M10 32l10-9M36 32l-10-9" stroke="#d32f1e" stroke-width="2" fill="none"/></svg>
</div>
<div class="abs hero-art" role="img" aria-label="Stacked browser windows showing search result pages under a magnifying glass"></div>

<!-- Categories -->
<div class="abs icon-disc" style="left:86px;top:433px;width:34px;height:34px"></div>
<h2 class="abs section-title" style="left:125px;top:438px">Cate<em>gories</em></h2>
<ul class="abs cat-list">
  <li class="cat-main">Developing a sales strategy</li>
  <li class="cat-main">Identifying the value proposition</li>
  <li class="cat-main">Focusing on the target market</li>
  <li class="cat-main">Analysing products/services</li>
  <li class="cat-sub">Assessing operational readiness</li>
  <li class="cat-sub">Creating a product/brand</li>
  <li class="cat-sub">Developing product channels</li>
  <li class="cat-sub">Establishing processes for</li>
  <li class="cat-main">Assessing operational readiness</li>
  <li class="cat-main">Creating a product/brand</li>
</ul>

<!-- Login -->
<div class="abs panel" style="left:91px;top:778px;width:195px;height:155px;background:#ececec;border:1px solid #fff"></div>
<div class="abs icon-disc" style="left:94px;top:780px;width:34px;height:34px"></div>
<h2 class="abs section-title" style="left:135px;top:790px;font-size:16px">Login <em>Form</em></h2>
<div class="abs rule" style="left:135px;top:813px;width:132px"></div>
<div class="abs field-label" style="left:76px;top:827px">Name :</div>
<div class="abs field" style="left:144px;top:823px;width:131px;height:21px;background:#fff"></div>
<div class="abs field-label" style="left:76px;top:859px">Email :</div>
<div class="abs field" style="left:143px;top:853px;width:131px;height:21px;background:#fff"></div>
<div class="abs" style="left:149px;top:886px;width:11px;height:11px;background:#fff;border:1px solid #ccc"></div>
<div class="abs" style="left:165px;top:886px;font-size:10px;color:#888">Remember</div>
<div class="abs pill-btn" style="left:200px;top:916px;width:71px;height:25px;line-height:22px">Login</div>

<!-- Welcome -->
<div class="abs icon-disc" style="left:314px;top:441px;width:34px;height:34px"></div>
<svg class="abs" style="left:323px;top:450px" width="16" height="14" viewBox="0 0 16 14"><path d="M8 1L1 7h2v6h4V9h2v4h4V7h2z" fill="#fff"/></svg>
<h2 class="abs section-title" style="left:353px;top:444px">Welcome to <em>Our Website</em></h2>
<div class="abs rule" style="left:353px;top:471px;width:457px"></div>
<div class="abs intro">
  <p><strong>Lorem Ipsum is simply dummy text of the printing and typesetting industry. Lorem Ipsum has been the industry's standard</strong> dummy text ever since the 1500s, when an unknown printer took a galley of type and scrambled it to make a type specimen book. It has survived not only five centuries,</p>
  <p>Lorem Ipsum is simply dummy text of the printing and typesetting industry. Lorem Ipsum has been the industry's standard dummy text ever since the 1500s, when an unknown printer took a galley of type</p>
</div>
<ol class="abs points">
  <li><span class="num">1.</span><span><b>Nascetur ridiculus mus.</b> Nulla fusce fegiat pharetra malesada</span></li>
  <li><span class="num">2.</span><span><b>Gravida at cursus luctus alorem.</b> Maecenas pharetra tristiqusit</span></li>
  <li><span class="num">3.</span><span><b>Duis ultricies pharetra magna.</b> Donec acumsan sit malesa</span></li>
  <li><span class="num">4.</span><span><b>Nascetur ridiculus mus.</b> Nulla fusce feugiat gamet malesuada</span></li>
  <li><span class="num">5.</span><span><b>Gravida at cursus luctus alorem.</b> Maecnas tristique amet</span></li>
</ol>

<!-- Projects -->
<h2 class="abs section-title" style="left:321px;top:724px">Latest <em>Projects</em></h2>
<div class="abs view-more">View more[+]</div>

<article class="abs card" style="left:313px">
  <span class="icon-disc"></span>
  <h3 class="card-title"><em>Software</em> Support</h3>
  <div class="rule"></div>
  <div class="card-img" role="img" aria-label="Support agent with headset at a desk" style="background:linear-gradient(120deg,#6b6f63,#c8b79a 55%,#e8e2d4)"></div>
  <p class="card-text"><strong>Lorem Ipsum is simply</strong> dummy text of the printing <b>[+]</b></p>
</article>
<article class="abs card" style="left:514px">
  <span class="icon-disc"></span>
  <h3 class="card-title"><em>Computer</em> Support</h3>
  <div class="rule"></div>
  <div class="card-img" role="img" aria-label="Two colleagues reviewing work at a laptop" style="background:linear-gradient(120deg,#3e4450,#a9adb3 55%,#e6e6e6)"></div>
  <p class="card-text"><strong>Lorem Ipsum is simply</strong> dummy text of the printing <b>[+]</b></p>
</article>
<article class="abs card" style="left:712px">
  <span class="icon-disc"></span>
  <h3 class="card-title"><em>Online</em> Support</h3>
  <div class="rule"></div>
  <div class="card-img" role="img" aria-label="Hands typing on a laptop holding a payment card" style="background:linear-gradient(120deg,#b7c8da,#dfe6ee 55%,#d96a3a)"></div>
  <p class="card-text"><strong>Lorem Ipsum is simply</strong> dummy text of the printing <b>[+]</b></p>
</article>

<!-- Footer -->
<footer class="abs site-footer"></footer>
<div class="abs footer-band"></div>
<h3 class="abs footer-title" style="left:105px">Our Tweets</h3>
<h3 class="abs footer-title" style="left:395px">Contact</h3>
<h3 class="abs footer-title" style="left:626px">Stay Up To Date!</h3>

<svg class="abs msg-icon" style="left:107px;top:1068px" viewBox="0 0 22 20"><path d="M3 2h16a2 2 0 0 1 2 2v9a2 2 0 0 1-2 2H9l-5 4v-4H3a2 2 0 0 1-2-2V4a2 2 0 0 1 2-2z" fill="#e6ebf2"/></svg>
<div class="abs footer-text" style="left:145px;top:1063px">Lorem ipsum dolor sit amet, consectetur</div>
<div class="abs tweet-date" style="left:145px;top:1087px">April 3, 2011</div>
<div class="abs footer-sep" style="left:105px;top:1106px;width:250px"></div>
<svg class="abs msg-icon" style="left:107px;top:1120px" viewBox="0 0 22 20"><path d="M3 2h16a2 2 0 0 1 2 2v9a2 2 0 0 1-2 2H9l-5 4v-4H3a2 2 0 0 1-2-2V4a2 2 0 0 1 2-2z" fill="#e6ebf2"/></svg>
<div class="abs footer-text" style="left:145px;top:1114px">Lorem ipsum dolor sit amet, consectetur</div>
<div class="abs tweet-date" style="left:145px;top:1138px">April 3, 2011</div>

<address class="abs footer-text" style="left:397px;top:1064px;font-style:normal">
  Northgate Partners, L.L.C.<br>
  2200 W. Harbor Ave. Suite 210<br>
  Lakeview, OR 97630<br>
  <span class="hl">Phone:</span> 480-555-0199<br>
  <span class="hl">Email:</span> info@brightharbor.example
</address>

<p class="abs footer-text" style="left:627px;top:1065px;width:250px">Lorem ipsum dolor sit amet, consectetur adipisicing elit, sed do eiusmod tempor incididunt ut labore et</p>
<div class="abs signup"><span>your email</span><b>Sign Up!</b></div>

<div class="abs footer-sep" style="left:0;top:1164px;width:960px"></div>
<div class="abs footer-text" style="left:105px;top:1176px">Copyright@BrightHarbor.example 2011 All rights reserved</div>
<div class="abs footer-links">home legal help support</div>

</body>
</html>
```